Tallymint - A/B testing for professionals

We need to improve the presentation layer (design only) of our tool tallymint.example.

www.tallymint.example is a A/B testing tool for websites and all kind of applications. The most important features are already listed on our actual webpage and the attached screenshots.
the animated icons on the front page should be included into the design and should match the color scheme. if you think you need to add a logo or similar things to it - feel free to offer us good proposals. you can reach us by sending us a mail to: support@tallymint.example

our needs listed:
-we'd rather have a very good improvement of the actual design instead of a big redesign with all colours changed etc.
- the pages in the screenshots attached should be redesigned. The amount of different layouts will be around 2 - 4 depending on the design.
- the animated icons on www.tallyrmint.example must be included into the design.
- the colors should match with the animated icons.
- we won't need any code. Psd / ai / graphic files only.

Target Market(s)

everyone who sells something with their webpage / application.

Number of Pages Required

3 page

Colors
85cae6
3276b5
85abd2
cee9f5
eaf1f7
0455a3
000000
0492cd

Requirements
Must have
• - animated icons included on the main page.
• - color match with the animated icons on our website or good proposal for adjusting them accordingly.
• - touch of that is highly scaleable and adjustable: we invented a new query language for the project
• - sweetness of the modern web projects and libraries
• - touch that the date are not shared between different users - high value on privacy
Nice to have
• - proposal for a matching logo or including the actual properly
Should not have
• - images people in the design
• - coded versions

```html
<!DOCTYPE html>
<html lang="en">
<head>
<meta charset="utf-8">
<title>Tallymint – A/B testing made for professionals</title>
<link rel="stylesheet" href="https://fonts.googleapis.com/css2?family=Open+Sans:wght@300;400;600&family=Source+Code+Pro:wght@400&display=swap">
<style>
:root{
  --nav:#4aa6cc;
  --hero:#58595b;
  --sea:#7fcbe0;
  --accent:#5ab4d6;
  --accent-dark:#3276b5;
  --pale:#eaf6fb;
  --text:#333;
  --muted:#8d8d8d;
  --rule:#dcdcdc;
  --footer:#5f5f61;
  --footer-bottom:#4a4a4c;
  --white:#fff;
  --code-tag:#881280;
  --code-attr:#994500;
  --code-val:#1a1aa6;
  --code-comment:#236e25;
}
*{box-sizing:border-box;margin:0;padding:0}
html,body{width:1200px;height:2403px;overflow:hidden}
body{position:relative;background:var(--white);font-family:"Open Sans",Arial,sans-serif;font-weight:300;color:var(--text)}
.abs{position:absolute}

/* nav */
.topbar{left:0;top:0;width:1200px;height:30px;background:var(--nav);color:var(--white)}
.brand{left:19px;top:4px;font-size:17px;font-weight:300}
.brand b{font-weight:600}
.topbar-links{right:20px;top:7px;font-size:12px;font-weight:400;display:flex;gap:20px}

/* hero */
.hero{left:0;top:30px;width:1200px;height:320px;background:var(--hero)}
.hero-title{left:0;top:48px;width:1200px;text-align:center;color:#bfe8f5;font-size:54px;font-weight:300;letter-spacing:.5px}
.hero-title b{font-weight:400}
.hero-sub{left:0;top:120px;width:1200px;text-align:center;color:var(--white);font-size:26px}
.hero-btn{left:538px;top:198px;width:122px;height:32px;background:var(--accent);border:1px solid #8fd0e8;color:var(--white);font-size:13px;font-weight:400;text-align:center;line-height:30px}
.hero-note{left:0;top:239px;width:1200px;text-align:center;color:#dfe8ec;font-size:13px;font-weight:400}
.hero-scene{left:0;top:350px;width:1200px;height:163px;background:linear-gradient(180deg,#86d0e4 0%,#7cc8de 100%)}

/* editor panel */
.editor{left:200px;top:431px;width:801px;height:320px;background:var(--white);border:1px solid #cfcfcf;box-shadow:0 1px 3px rgba(0,0,0,.15);font-family:"Source Code Pro",monospace;font-size:9px;color:#222;overflow:hidden}
.editor-bar{height:22px;background:#eef1f4;border-bottom:1px solid #ccc;display:flex;align-items:stretch;font-family:"Open Sans",sans-serif;font-size:10px;font-weight:400}
.editor-bar .tab{padding:0 10px;display:flex;align-items:center;gap:5px;color:#444}
.editor-bar .tab.active{background:var(--accent);color:var(--white)}
.tab i{display:inline-block;width:10px;height:10px}
.editor-close{position:absolute;right:4px;top:4px;width:14px;height:14px;background:#d53a2c;color:#fff;font-size:11px;line-height:14px;text-align:center;font-family:"Open Sans",sans-serif}
.editor-min{position:absolute;right:24px;top:5px;width:14px;height:12px;background:#7fc3e0}
.dom{position:absolute;left:0;top:22px;width:391px;bottom:0;border-right:1px solid #ccc;padding:3px 0;line-height:11.5px}
.dom div{padding-left:6px;white-space:pre;height:11.5px}
.dom .sel{background:#4aa6cc;color:#fff}
.t{color:var(--code-tag)} .a{color:var(--code-attr)} .v{color:var(--code-val)} .c{color:var(--code-comment)}
.styles{position:absolute;left:392px;top:22px;right:0;bottom:0;line-height:11.5px}
.style-tabs{display:flex;gap:2px;padding:3px 3px 0;border-bottom:1px solid #ccc;font-family:"Open Sans",sans-serif;font-size:9px;font-weight:400}
.style-tabs span{padding:1px 6px;background:#e4e4e4}
.style-tabs span.on{background:var(--accent);color:#fff}
.states{position:relative;display:grid;grid-template-columns:100px 100px;padding:2px 4px;border-bottom:1px solid #ccc}
.states span::before{content:"";display:inline-block;width:7px;height:7px;border:1px solid #999;margin-right:6px;vertical-align:-1px}
.states .toggle{position:absolute;right:18px;top:5px;width:14px;height:14px;border-radius:50%;background:var(--accent)}
.rule{display:flex;justify-content:space-between;padding:2px 2px;border-bottom:1px solid #ddd}
.rule em{font-style:normal;color:#888}
.rule u{color:#888}
.block{padding:6px 2px;white-space:pre}

/* tabs under editor */
.editor-tabs{left:0;top:770px;width:1200px;display:flex;justify-content:center;gap:30px;font-size:15px;font-weight:400;color:#9fd2e6}
.editor-tabs .on{color:var(--accent)}

/* intro */
.intro{left:0;top:848px;width:1200px;text-align:center;font-size:20px;line-height:31px;color:#444}
.intro b{font-weight:400;color:#111}

/* features */
.features{left:0;top:961px;width:1200px;height:518px;background:var(--pale)}
.feature{width:230px;text-align:center}
.feature .ico{display:block;margin:0 auto}
.feature h3{margin-top:6px;font-size:19px;font-weight:300;color:var(--accent)}
.feature p{margin-top:8px;font-size:12.5px;line-height:19px;color:var(--muted);font-weight:400}
.feature p b{color:#666;font-weight:600}

/* showcase rows */
.illus{border-radius:4px}
.row-text{width:540px}
.row-text h2{font-size:21px;font-weight:400;color:#333}
.row-text p{margin-top:14px;font-size:12.5px;line-height:20px;color:#777;font-weight:400}
.row-text a{color:var(--accent);text-decoration:none}
kbd{font-family:"Source Code Pro",monospace;font-size:9px;border:1px solid #bbb;border-radius:3px;padding:1px 4px;color:#444;background:#f6f6f6}

/* footer */
.footer{left:0;top:2232px;width:1200px;height:147px;background:var(--footer);color:#fff}
.foot-col{top:28px;font-size:13px;font-weight:400}
.foot-col ul{list-style:none;margin-top:5px}
.foot-col li{font-size:11.5px;line-height:19px;color:#8fcfe8}
.foot-divider{top:30px;width:1px;height:80px;background:#6f6f71}
.social{left:410px;top:122px;display:flex;gap:12px}
.social span{width:17px;height:17px;border-radius:50%;background:#cfd6da}
.foot-bottom{left:0;top:2379px;width:1200px;height:24px;background:var(--footer-bottom);color:#eee;font-size:11px;font-weight:400;text-align:center;line-height:24px}
</style>
</head>
<body>

<header class="abs topbar">
  <div class="abs brand">Tally<b>mint</b></div>
  <nav class="abs topbar-links"><span>Install</span><span>Login</span></nav>
</header>

<section class="abs hero">
  <h1 class="abs hero-title">Tally<b>mint</b></h1>
  <p class="abs hero-sub">A/B testing made for professionals</p>
  <div class="abs hero-btn">Install &amp; Configure</div>
  <p class="abs hero-note">Start improving your conversion rate.</p>
</section>
<div class="abs hero-scene" role="img" aria-label="Illustrated landscape of pale blue sail-shaped peaks with small red flags beneath white clouds"></div>

<div class="abs editor">
  <div class="editor-bar">
    <div class="tab"><i style="background:#e0a93a;border-radius:50%"></i></div>
    <div class="tab active"><i style="background:#9fe0a0"></i>Elements</div>
    <div class="tab"><i style="background:#e05a3a"></i>Changes</div>
    <div class="tab"><i style="background:#f0b040"></i>Experiment</div>
  </div>
  <div class="editor-min"></div>
  <div class="editor-close">×</div>
  <div class="dom"><div><span class="t">&lt;!DOCTYPE html&gt;</span></div><div>▼ <span class="t">&lt;html</span> <span class="a">class</span>=<span class="v">"teaser"</span> <span class="a">lang</span>=<span class="v">"en-ch"</span><span class="t">&gt;</span></div><div>   ▶ <span class="t">&lt;head&gt;</span>…<span class="t">&lt;/head&gt;</span></div><div>   ▼ <span class="t">&lt;body</span> <span class="a">cz-shortcut-listen</span>=<span class="v">"true"</span><span class="t">&gt;</span></div><div>        <span class="c">&lt;!-- Share Button etc.--&gt;</span></div><div>      ▶ <span class="t">&lt;div</span> <span class="a">id</span>=<span class="v">"share-root"</span> <span class="a">class</span>=<span class="v">" share_reset"</span><span class="t">&gt;</span>…<span class="t">&lt;/div&gt;</span></div><div>      ▶ <span class="t">&lt;script&gt;</span>…<span class="t">&lt;/script&gt;</span></div><div>        <span class="c">&lt;!-- End Share Button etc.--&gt;</span></div><div>      ▶ <span class="t">&lt;header&gt;</span>…<span class="t">&lt;/header&gt;</span></div><div class="sel">      ▶ &lt;main&gt;…&lt;/main&gt;</div><div>        <span class="t">&lt;script</span> <span class="a">src</span>=<span class="v">"/Scripts/ja?</span></div><div>        <span class="v">v=ZwSHqfabuYxSpCrWyOwNIh4gAhvi7IV5c968qId5egol"</span><span class="t">&gt;</span></div><div>     <span class="t">&lt;/body&gt;</span></div></div>
  <div class="styles">
    <div class="style-tabs"><span class="on">CSS</span><span>Text</span><span>Attributes</span><span>Html</span></div>
    <div class="states"><span>:hover</span><span>:focus</span><span>:visited</span><span>:active</span><i class="toggle"></i></div>
    <div class="rule"><span>element.style { }</span><em>readonly</em></div>
    <div class="block">.teaser main {                                <u>prettify.css</u>
   height: 100%;
   margin-top: 60px;
   text-align: center;
   border: 1px solid black;
}</div>
  </div>
</div>

<nav class="abs editor-tabs">
  <span class="on">Editor</span><span>Standard Reports</span><span>Queries</span><span>Custom Reports</span>
</nav>

<p class="abs intro"><b>Tally</b>mint is a testing tool which measures influence of changes made to your website.<br>Probability and statistics will help you to progressively improve.</p>

<section class="abs features">
  <div class="abs feature" style="left:224px;top:58px">
    <svg class="ico" width="62" height="62" viewBox="0 0 62 62"><circle cx="31" cy="31" r="31" fill="#5ab4d6"/><rect x="18" y="33" width="16" height="11" fill="#fff"/><path d="M30 36 L44 18 L48 21 L34 39 Z" fill="#f0a040"/></svg>
    <h3>Create Experiments</h3>
    <p>Use the editor to create experiments by changing texts, attributes and styling. Write JavaScript, or do server side experiments.</p>
  </div>
  <div class="abs feature" style="left:484px;top:58px">
    <svg class="ico" width="62" height="62" viewBox="0 0 62 62"><circle cx="31" cy="31" r="31" fill="#5ab4d6"/><path d="M20 32 L34 18 L46 18 L46 30 L32 44 Z" fill="#f0a040"/><circle cx="41" cy="23" r="2.5" fill="#fff"/></svg>
    <h3>Tags</h3>
    <p>By tagging your experiments into categories and strategies, you will be able to measure how well the whole improvement strategy works.</p>
  </div>
  <div class="abs feature" style="left:744px;top:58px">
    <svg class="ico" width="62" height="62" viewBox="0 0 62 62"><circle cx="31" cy="31" r="31" fill="#5ab4d6"/><ellipse cx="31" cy="31" rx="17" ry="11" fill="#fff"/><circle cx="31" cy="31" r="7" fill="#e0703a"/><circle cx="31" cy="31" r="3" fill="#3276b5"/></svg>
    <h3>Preview</h3>
    <p>All users can freely turn on their previewed experiments, which will be visible on the product just like any other user would see it.</p>
  </div>
  <div class="abs feature" style="left:224px;top:278px">
    <svg class="ico" width="62" height="62" viewBox="0 0 62 62"><circle cx="31" cy="31" r="31" fill="#5ab4d6"/><g fill="#3276b5"><rect x="19" y="35" width="8" height="8"/><rect x="28" y="35" width="8" height="8"/><rect x="37" y="35" width="8" height="8"/><rect x="23" y="26" width="8" height="8"/><rect x="32" y="26" width="8" height="8"/><rect x="28" y="17" width="8" height="8"/></g></svg>
    <h3>Fields</h3>
    <p>Any tracking, goals, events or values can be stored in a data field, which will be automatically available in your reports.</p>
  </div>
  <div class="abs feature" style="left:484px;top:278px">
    <svg class="ico" width="62" height="62" viewBox="0 0 62 62"><circle cx="31" cy="31" r="31" fill="#5ab4d6"/><path d="M17 20 L30 22 L30 44 L17 42 Z" fill="#fff"/><path d="M45 20 L32 22 L32 44 L45 42 Z" fill="#eef6fa"/></svg>
    <h3>Reports</h3>
    <p>Use our standard reports or create custom reports with widgets using our query language <b>DQL</b>.</p>
  </div>
  <div class="abs feature" style="left:744px;top:278px">
    <svg class="ico" width="62" height="62" viewBox="0 0 62 62"><circle cx="31" cy="31" r="31" fill="#5ab4d6"/><path d="M17 32 L45 18 L36 44 L31 35 Z" fill="#fff"/><path d="M31 35 L45 18 L29 42 Z" fill="#cde6f2"/></svg>
    <h3>Queries</h3>
    <p>Write your own queries. you're able to select all the data which we save and you can use them in the way you need them.</p>
  </div>
</section>

<div class="abs illus" style="left:200px;top:1530px;width:225px;height:192px;background:radial-gradient(ellipse at 50% 85%,#8fd0e6 0 32%,transparent 33%),linear-gradient(180deg,#f3f4f5,#dfe3e6)" role="img" aria-label="Illustration of an isometric office building on a pale blue round base"></div>
<div class="abs row-text" style="left:464px;top:1578px">
  <h2>Create experiments directly on the webproduct</h2>
  <p>The installation of Tallymint enables a keyboard shortcut <kbd>CTRL + ALT + E</kbd> on the website. Using this shortcut it is easily possible to create lots of experiments. As long as logged in on Tallymint this shortcut <a>will open the editor</a> and it will assist for special desires.</p>
</div>

<div class="abs row-text" style="left:200px;top:1802px">
  <h2>Check results with available reports</h2>
  <p>There are <a>quite a few reports available</a> to analyse results. Especially the system wide reports which make use of hashtags are really helpful to find out what the users desire. And even if those system reports are insufficient, Tallymint supports custom reports!</p>
</div>
<div class="abs illus" style="left:764px;top:1762px;width:237px;height:176px;background:radial-gradient(ellipse at 50% 82%,#8fd0e6 0 34%,transparent 35%),linear-gradient(180deg,#f1f4f6,#dde3e7)" role="img" aria-label="Illustration of a large monitor showing a line chart on a pale blue round base"></div>

<div class="abs illus" style="left:200px;top:2010px;width:225px;height:160px;background:radial-gradient(ellipse at 50% 78%,#8fd0e6 0 34%,transparent 35%),linear-gradient(180deg,#f3f4f5,#dfe3e6)" role="img" aria-label="Illustration of a low isometric building on a pale blue round base"></div>
<div class="abs row-text" style="left:464px;top:2025px">
  <h2>Flexible analysis using DQL</h2>
  <p>Tallymint introduces a <a>draw query language (DQL)</a> which is more or less the same as SQL with an output solution. This language is easy to learn, and allows reading the users mind by just painting the data in fancy charts!</p>
</div>

<footer class="abs footer">
  <div class="abs foot-col" style="left:410px">Documentation<ul><li>Guides</li><li>Query Docs</li><li>Report Docs</li></ul></div>
  <div class="abs foot-divider" style="left:532px"></div>
  <div class="abs foot-col" style="left:546px">Information<ul><li>Ask Questions</li><li>Answer Questions</li><li>Official Blog</li></ul></div>
  <div class="abs foot-divider" style="left:668px"></div>
  <div class="abs foot-col" style="left:682px">About<ul><li>Privacy</li><li>Contact</li><li>About us</li></ul></div>
  <div class="abs foot-divider" style="left:802px"></div>
  <div class="abs social" aria-label="Social links"><span></span><span></span></div>
</footer>
<div class="abs foot-bottom">© Tallymint</div>

</body>
</html>
```